Business card design needed for Renewable utilities company based in New Zealand.

We supply and install solar panels and all components along with it for a fully customisable PV system that helps customer save money on their energy bills right away and also save the planet!

I have attached logo & website design files to give you a better insight.

Industry/Entity Type

Business

```html
<!DOCTYPE html>
<html lang="en">
<head>
<meta charset="utf-8">
<title>Sunhaven Power – Business Card</title>
<link href="https://fonts.googleapis.com/css2?family=Open+Sans:wght@400;600&display=swap" rel="stylesheet">
<style>
  :root {
    --backdrop: #e6e6e8;
    --card-white: #f7f7f8;
    --navy: #1f3566;
    --navy-light: #3c5f95;
    --band: #34489a;
    --sky: #1e9ad6;
    --ink: #2c2c30;
    --ink-soft: #55565c;
  }
  * { box-sizing: border-box; margin: 0; padding: 0; }
  html, body { width: 1200px; height: 1000px; overflow: hidden; }
  body {
    background: var(--backdrop);
    font-family: "Open Sans", Arial, sans-serif;
    position: relative;
  }
  .card {
    position: absolute;
    width: 520px;
    height: 300px;
    border-radius: 26px;
    overflow: hidden;
    box-shadow: 0 6px 18px rgba(0,0,0,0.18);
  }
  .brand {
    position: absolute;
    left: 0; right: 0;
    display: flex; flex-direction: column; align-items: center; gap: 12px;
  }
  .brand-dot { border-radius: 50%; }
  .brand-name { font-weight: 400; letter-spacing: 0.5px; white-space: nowrap; }

  /* front */
  .card-front {
    left: 90px; top: 150px;
    background: linear-gradient(135deg, #ffffff 0%, var(--card-white) 55%, #ececee 100%);
  }
  .card-front .brand { top: 48px; }
  .card-front .brand-dot { width: 70px; height: 70px; background: var(--navy); }
  .card-front .brand-name { font-size: 38px; line-height: 1.2; color: var(--sky); }
  .tagline-band {
    position: absolute; left: 0; right: 0; top: 222px;
    height: 30px;
    background: var(--band);
    color: #fff;
    font-size: 15px; font-weight: 600;
    display: flex; align-items: center; justify-content: center;
    letter-spacing: 0.3px;
  }

  /* back */
  .card-back {
    left: 590px; top: 560px;
    background: var(--card-white);
    display: flex;
  }
  .back-panel {
    position: relative;
    flex: none;
    width: 280px; height: 100%;
    background: radial-gradient(circle at 35% 25%, var(--navy-light) 0%, var(--navy) 70%);
  }
  .card-back .brand { top: 108px; }
  .card-back .brand-dot { background: #fff; width: 56px; height: 56px; }
  .card-back .brand-name { font-size: 28px; line-height: 1.2; color: #fff; }
  .contact {
    padding: 34px 16px 0 22px;
    color: var(--ink);
    font-size: 12.5px;
    line-height: 1.36;
    min-width: 0;
  }
  .person-name { font-size: 18px; color: var(--ink); }
  .person-name .surname { color: var(--sky); font-weight: 600; }
  .person-role { color: var(--ink-soft); font-size: 12.5px; margin-bottom: 22px; }
  .address { margin-bottom: 14px; }
  .contact-line { display: flex; align-items: center; gap: 6px; white-space: nowrap; }
  .contact-line svg { width: 12px; height: 12px; flex: none; }
  .web { padding-left: 18px; white-space: nowrap; }
</style>
</head>
<body>

  <section class="card card-front" aria-label="Business card front">
    <div class="brand">
      <span class="brand-dot"></span>
      <span class="brand-name">Sunhaven Power</span>
    </div>
    <div class="tagline-band">The Best Solar Energy Specialists in New Zealand!</div>
  </section>

  <section class="card card-back" aria-label="Business card back">
    <div class="back-panel">
      <div class="brand">
        <span class="brand-dot"></span>
        <span class="brand-name">Sunhaven Power</span>
      </div>
    </div>
    <div class="contact">
      <p class="person-name">Sam <span class="surname">Carter</span></p>
      <p class="person-role">Director</p>
      <p class="address">27 Harbour Lane<br>Auckland 1010<br>PO Box 000</p>
      <p class="contact-line">
        <svg viewBox="0 0 16 16" aria-hidden="true"><path fill="#2c2c30" d="M3 1.5l2.5 0 1 3.5-1.6 1.2a9 9 0 0 0 4.9 4.9L11 9.5l3.5 1v2.5c0 .8-.7 1.5-1.5 1.5A12.5 12.5 0 0 1 1.5 3C1.5 2.2 2.2 1.5 3 1.5z"/></svg>
        0800-555-0142
      </p>
      <p class="contact-line">
        <svg viewBox="0 0 16 16" aria-hidden="true"><rect x="1" y="3" width="14" height="10" fill="#2c2c30"/><path d="M1.5 3.5 L8 9 L14.5 3.5" stroke="#fff" stroke-width="1.2" fill="none"/></svg>
        s.carter@sunhavenpower.com
      </p>
      <p class="web">www.sunhavenpower.com</p>
    </div>
  </section>

</body>
</html>
```